stationary and business cards for vending company
brightsnak
stationary and business cards for vending company - Food
Creative Brief
Bright & Fun-filled
Milo Fenwick
General Manager
Suite 418 Calloway Court 27 Mill Lane Epsom Surrey KT19 4QP
m.fenwick@brightsnak.co.uk
www.brightsnak.co.uk

```html
<!DOCTYPE html>
<html lang="en">
<head>
<meta charset="utf-8">
<title>brightsnak stationery</title>
<link rel="stylesheet" href="https://fonts.googleapis.com/css2?family=Nunito:wght@400;700&display=swap">
<style>
  :root{
    --bg:#f3f4f6;
    --paper:#ffffff;
    --edge:#dde1e6;
    --blue-deep:#0e4d9c;
    --blue:#1e73c8;
    --blue-light:#6fb3ea;
    --green:#7cc242;
    --ink:#4a5563;
    --pen:#1d3e7a;
  }
  html,body{margin:0;padding:0;overflow:hidden;}
  body{width:1200px;height:228px;background:var(--bg);font-family:"Nunito",sans-serif;}
  .stationery-set{display:block;width:1200px;height:228px;}
  .brand{font-family:"Nunito",sans-serif;font-weight:700;fill:var(--blue);}
  .brand-light{font-family:"Nunito",sans-serif;font-weight:700;fill:var(--paper);}
  .tag{font-family:"Nunito",sans-serif;font-size:3px;fill:var(--blue-light);}
  .body-text{font-family:"Nunito",sans-serif;font-size:3.2px;fill:var(--ink);}
  .small-text{font-family:"Nunito",sans-serif;font-size:2.6px;fill:var(--ink);}
  .small-light{font-family:"Nunito",sans-serif;font-size:2.6px;fill:#dbe9f8;}
  .sheet{fill:var(--paper);stroke:var(--edge);}
  .band{fill:url(#bandFill);}
</style>
</head>
<body>
<svg class="stationery-set" viewBox="0 0 1200 228" xmlns="http://www.w3.org/2000/svg">
  <defs>
    <linearGradient id="blueFill" x1="0" y1="0" x2="0" y2="1">
      <stop offset="0" stop-color="#2a86d6"/>
      <stop offset="1" stop-color="#0c4a96"/>
    </linearGradient>
    <linearGradient id="bandFill" x1="0" y1="0" x2="1" y2="0">
      <stop offset="0" stop-color="#0e4d9c"/>
      <stop offset="1" stop-color="#4aa3e6"/>
    </linearGradient>
    <g id="brand-mark">
      <circle cx="0" cy="0" r="3.2" fill="var(--green)"/>
      <text class="brand" x="5" y="2.6" font-size="8">brightsnak</text>
    </g>
  </defs>

  <!-- phone screen -->
  <g class="phone">
    <rect x="8" y="58" width="28" height="106" rx="5" fill="#e9ebef" stroke="#c9cdd3"/>
    <rect x="11" y="68" width="22" height="84" fill="url(#blueFill)"/>
    <circle cx="22" cy="100" r="1.6" fill="var(--green)"/>
    <text class="brand-light" x="22" y="108" font-size="3.6" text-anchor="middle">brightsnak</text>
  </g>

  <!-- business cards -->
  <g class="business-cards">
    <rect class="sheet" x="44" y="54" width="54" height="32"/>
    <use href="#brand-mark" transform="translate(52 66) scale(0.55)"/>
    <rect class="band" x="44" y="80" width="54" height="6"/>
    <rect x="44" y="92" width="54" height="32" fill="url(#blueFill)"/>
    <text class="brand-light" x="71" y="110" font-size="5" text-anchor="middle">brightsnak</text>
    <rect class="sheet" x="44" y="130" width="54" height="32"/>
    <text class="small-text" x="48" y="138" font-weight="700">Milo Fenwick</text>
    <text class="small-text" x="48" y="142">General Manager</text>
    <text class="small-text" x="48" y="148">m.fenwick@brightsnak.co.uk</text>
    <text class="small-text" x="48" y="152">www.brightsnak.co.uk</text>
    <rect class="band" x="44" y="156" width="54" height="6"/>
    <rect x="44" y="168" width="54" height="32" fill="url(#blueFill)"/>
  </g>

  <!-- letterhead one -->
  <g class="letterhead">
    <rect class="sheet" x="106" y="10" width="115" height="211"/>
    <use href="#brand-mark" transform="translate(166 22) scale(0.9)"/>
    <text class="tag" x="171" y="30">fresh snacks daily</text>
    <text class="body-text" x="116" y="46">Dear Client,</text>
    <text class="body-text" x="116" y="54">Thank you for choosing our vending service. We keep</text>
    <text class="body-text" x="116" y="59">your break room stocked with fresh snacks and cold</text>
    <text class="body-text" x="116" y="64">drinks every week.</text>
    <text class="body-text" x="116" y="74">Kind regards</text>
    <rect class="band" x="106" y="204" width="115" height="17"/>
    <text class="small-light" x="163.5" y="214" text-anchor="middle">Suite 418 Calloway Court 27 Mill Lane Epsom Surrey KT19 4QP</text>
  </g>

  <!-- letterhead two -->
  <g class="letterhead">
    <rect class="sheet" x="233" y="10" width="115" height="211"/>
    <use href="#brand-mark" transform="translate(293 22) scale(0.9)"/>
    <rect class="band" x="233" y="204" width="115" height="17"/>
    <text class="small-light" x="290.5" y="214" text-anchor="middle">www.brightsnak.co.uk</text>
  </g>

  <!-- envelopes -->
  <g class="envelopes">
    <rect class="sheet" x="360" y="30" width="132" height="34"/>
    <path d="M360 30 L426 52 L492 30" fill="none" stroke="var(--edge)"/>
    <rect class="sheet" x="360" y="70" width="132" height="38"/>
    <use href="#brand-mark" transform="translate(368 80) scale(0.6)"/>
    <rect class="band" x="360" y="100" width="132" height="8"/>
  </g>

  <!-- compliment slips -->
  <g class="compliment-slips">
    <rect class="sheet" x="372" y="116" width="108" height="30"/>
    <use href="#brand-mark" transform="translate(402 128) scale(0.7)"/>
    <rect class="band" x="372" y="140" width="108" height="6"/>
    <rect x="372" y="152" width="108" height="30" fill="url(#blueFill)"/>
    <text class="brand-light" x="426" y="169" font-size="6" text-anchor="middle">brightsnak</text>
  </g>

  <!-- small cards -->
  <g class="tags">
    <rect class="sheet" x="496" y="56" width="34" height="20"/>
    <text class="brand" x="513" y="68" font-size="4" text-anchor="middle">brightsnak</text>
    <rect x="496" y="82" width="34" height="20" fill="url(#blueFill)"/>
  </g>

  <!-- disc case and disc -->
  <g class="disc">
    <rect x="536" y="48" width="74" height="82" fill="url(#blueFill)"/>
    <text class="brand-light" x="554" y="60" font-size="5" text-anchor="middle">brightsnak</text>
    <circle cx="612" cy="100" r="40" fill="url(#blueFill)" stroke="#d7dde5"/>
    <circle cx="612" cy="100" r="12" fill="var(--bg)" stroke="#c9cdd3"/>
    <circle cx="612" cy="100" r="5" fill="var(--paper)"/>
    <text class="brand-light" x="612" y="128" font-size="5" text-anchor="middle">brightsnak</text>
  </g>

  <!-- pencil placeholder -->
  <rect class="pen" x="612" y="156" width="76" height="4" fill="var(--pen)" transform="rotate(-48 650 158)" role="img" aria-label="Branded pencil"/>

  <!-- presentation sheet -->
  <g class="presentation-sheet">
    <rect x="696" y="6" width="132" height="214" fill="url(#blueFill)"/>
    <circle cx="762" cy="26" r="3" fill="var(--green)"/>
    <text class="brand-light" x="762" y="40" font-size="9" text-anchor="middle">brightsnak</text>
  </g>

  <!-- folder -->
  <g class="folder">
    <rect class="sheet" x="950" y="10" width="115" height="211"/>
    <rect class="band" x="950" y="204" width="115" height="17"/>
    <rect x="1062" y="6" width="132" height="216" fill="url(#blueFill)"/>
    <circle cx="1100" cy="70" r="3" fill="var(--green)"/>
    <text class="brand-light" x="1106" y="73" font-size="9">brightsnak</text>
  </g>
</svg>
</body>
</html>
```